Large corporation needs landing page for its employees with emotional and psychological problems

Vision:
Hello, we are a startup and would like to build a landing page and website in the mental health sector for a large corporation. In this site employees with emotional and psychological problems should quickly receive professional psychological support. This support takes the form of internal referrals from employees who are looking for help to qualified therapists, so that help can be provided quickly.
Furthermore, the employees get access to a tool where they can find out about topics in the mind health area and can also get help via webinars and podcasts. The employee should thus be able to take the hurdle to seek help and support in good time.
Therapists for whom the focus is on the urgency of providing quick help and support will work here in cooperation with the respective corporations.
Keywords:
• Help/Support
• overcome inhibitions
• Competent help
• Uncomplicated help
• Permanent access
• protected space
• Recognizing and naming emotional problems and actively tackling them
• get help
• mindfulness
• everyday helper
• Informative
• Anonymous
• compassion
• tolerance
• respect
• Appreciation
• empathy
• mindfulness
• protected space
• To be needed
• Like a lighthouse signal
What we need:
Landingpage
We need a landing page aimed at getting employees to contact psychological help. The call to action is to get in contact via a contact form.
Landing page content
There are several text modules:
• A heading/greeting
• A body of text at the beginning that explains the purpose of the page
• A bulleted text area describing the pain points and the solutions to them
Video:
The heart of the content will be a video explaining the need and inviting them to get in touch.
contact form:
It should be kept simple: first name, last name and email address
Legally required content:
General terms and conditions, data protection and imprint. These are only given as links in the footer.
In parallel, the Corporate Design should be adapted/extended:
Logo:
The font in the logo should be revised. The wings in the background remain.
Please adapt the logo for different uses:
• on a black background
• with transparent background
• favorite icon (browser)
• In square format for social media
Colors:
• develop a color chart based on the colors of the logo.
• please determine 2-3 main colors and the matching variations. I.e. transparent variations or light colors.
Typography:
Determine a decorative font and/or typography for headings and a text font. There should be no more than 3 fonts.
Industry/Entity Type
to recruit therapists as employees
Requirements
Should not have
- please not to playful design or typography - and max. 3 colors

```html
<!DOCTYPE html>
<html lang="en">
<head>
<meta charset="utf-8">
<title>Calm Harbor – We are here for you</title>
<link href="https://fonts.googleapis.com/css2?family=Outfit:wght@400;500;600;700&display=swap" rel="stylesheet">
<style>
:root{
  --ink:#0b4656;
  --ink-dark:#043a48;
  --text:#1d2b30;
  --mint:#1de0b0;
  --mint-soft:#c9f3e7;
  --card-blue:#d7eef8;
  --card-mint:#d7f5ef;
  --card-aqua:#e7f8f8;
  --footer:#17282e;
  --stage:#e4f1ef;
  --white:#ffffff;
}
*{box-sizing:border-box;margin:0;padding:0}
html,body{width:1144px;height:1200px;overflow:hidden}
body{background:var(--stage);font-family:"Outfit",sans-serif;color:var(--text)}
.frame{position:absolute;left:259px;top:0;width:626px;height:1200px;overflow:hidden;box-shadow:0 10px 40px rgba(11,70,86,.12)}
.page{position:absolute;left:0;top:0;width:837px;height:1605px;background:var(--white);transform:scale(.7477);transform-origin:0 0}
.abs{position:absolute}

.hero-bg{left:0;top:0;width:837px;height:490px;background:linear-gradient(160deg,#d5f5ee 0%,#e6f8fb 40%,#e3f3fb 70%,#cfe2f6 100%)}

.brand{left:71px;top:26px;font-size:17px;font-weight:600;color:var(--ink);letter-spacing:.2px}
.nav{top:33px;font-size:9px;color:var(--text);font-weight:500}
.nav.active{font-weight:700}
.btn{display:flex;align-items:center;justify-content:center;background:var(--mint);color:var(--white);font-weight:600;font-size:9px;border-radius:2px}

.hero-title{left:0;width:837px;top:108px;text-align:center;font-size:40px;font-weight:700;color:var(--ink);letter-spacing:-.5px}
.hero-sub{left:0;width:837px;top:163px;text-align:center;font-size:13px;line-height:17px;color:var(--text)}

.video-frame{left:168px;top:280px;width:502px;height:289px;background:var(--mint-soft);border-radius:6px}
.video{left:182px;top:294px;width:475px;height:258px;border-radius:8px;background:linear-gradient(100deg,#1f2c48 0%,#2d3b58 25%,#9fb5ad 45%,#8e97a4 65%,#c3c4c8 85%,#a08f86 100%)}
.play{left:393px;top:389px;width:52px;height:52px;border-radius:50%;background:var(--white);display:flex;align-items:center;justify-content:center}

.card{top:610px;width:184px;height:203px;border-radius:3px;text-align:center;padding:0 14px}
.card svg{margin-top:28px}
.card h3{margin-top:18px;font-size:13px;line-height:17px;font-weight:600;color:var(--ink)}
.card p{margin-top:10px;font-size:10px;line-height:13px;color:var(--text)}

.section-title{left:130px;top:893px;font-size:28px;line-height:37px;font-weight:700;color:var(--ink);letter-spacing:-.3px}
.accent{color:var(--mint)}
.section-copy{left:130px;top:989px;width:295px;font-size:12.5px;line-height:17.5px}
.section-copy p+p{margin-top:17px}
.photo-back{left:536px;top:1005px;width:195px;height:235px;background:var(--card-mint);border-radius:3px}
.photo{left:484px;top:897px;width:225px;height:317px;border-radius:8px;background:linear-gradient(170deg,#e4e4e6 0%,#cfd3d4 35%,#8fa6a3 60%,#3a6a5c 80%,#1fa27f 100%)}

.band{left:0;top:1299px;width:837px;height:229px;background:var(--ink-dark)}
.band-title{left:0;width:837px;top:1340px;text-align:center;font-size:28px;font-weight:600;color:var(--white)}
.band-sub{left:0;width:837px;top:1385px;text-align:center;font-size:12.5px;color:#e6f2f3}
.field{top:1439px;height:26px;background:#f7f7f7;border-radius:2px;font-size:11px;color:#8a9497;padding:0 7px;display:flex;align-items:center}

.footer{left:0;top:1528px;width:837px;height:77px;background:var(--footer);display:flex;align-items:center;justify-content:center;font-size:10px;color:var(--white)}
.footer a{color:var(--mint);text-decoration:none}
</style>
</head>
<body>
<div class="frame">
<div class="page">

  <div class="abs hero-bg"></div>

  <div class="abs brand">calm harbor</div>
  <div class="abs nav active" style="left:198px">Home</div>
  <div class="abs nav" style="left:245px">Mental Health Resources ⌄</div>
  <div class="abs nav" style="left:378px">Doctors List</div>
  <div class="abs nav" style="left:449px">Blog</div>
  <div class="abs nav" style="left:649px">Login</div>
  <div class="abs btn" style="left:682px;top:24px;width:85px;height:27px">Ask for Help</div>

  <h1 class="abs hero-title">We are here for you.</h1>
  <p class="abs hero-sub">Dedicated support in recognizing and naming emotional problems<br>you have and solving them.</p>
  <div class="abs btn" style="left:376px;top:218px;width:85px;height:26px">Ask for Help</div>

  <div class="abs video-frame"></div>
  <div class="abs video" role="img" aria-label="Video still of a counselling conversation between two women"></div>
  <div class="abs play"><svg width="16" height="16" viewBox="0 0 16 16"><path d="M4 2 L14 8 L4 14 Z" fill="var(--mint)"/></svg></div>

  <div class="abs card" style="left:130px;background:var(--card-blue)">
    <svg width="48" height="44" viewBox="0 0 48 44" fill="none" stroke="var(--ink)" stroke-width="1.5">
      <path d="M24 40 C10 30 4 22 4 14 C4 8 9 4 14 4 C18 4 22 6 24 10 C26 6 30 4 34 4 C39 4 44 8 44 14 C44 22 38 30 24 40 Z"/>
      <circle cx="36" cy="30" r="7" fill="var(--mint)" stroke="none"/>
    </svg>
    <h3>Help and support during difficult times</h3>
    <p>Lorem ipsum dolor sit amet, consectetur adipiscing elit, sed do eiusmod</p>
  </div>
  <div class="abs card" style="left:327px;background:var(--card-mint)">
    <svg width="48" height="44" viewBox="0 0 48 44" fill="none" stroke="var(--ink)" stroke-width="1.5">
      <circle cx="14" cy="12" r="8" fill="var(--mint)" stroke="none"/>
      <rect x="10" y="8" width="28" height="30" rx="4"/>
      <path d="M24 15 V31 M16 23 H32"/>
    </svg>
    <h3>Competent help from health professionals</h3>
    <p>Lorem ipsum dolor sit amet, consectetur adipiscing elit, sed do eiusmod</p>
  </div>
  <div class="abs card" style="left:524px;background:var(--card-aqua)">
    <svg width="56" height="44" viewBox="0 0 56 44" fill="none" stroke="var(--ink)" stroke-width="1.5">
      <path d="M6 36 V8 H20 L24 12 H44 V18"/>
      <path d="M6 36 L14 18 H52 L44 36 Z"/>
      <path d="M29 21 H33 V25 H37 V29 H33 V33 H29 V29 H25 V25 H29 Z"/>
      <circle cx="8" cy="34" r="7" fill="var(--mint)" stroke="none"/>
    </svg>
    <h3>Lifetime access to all of our health resources</h3>
    <p>Lorem ipsum dolor sit amet, consectetur adipiscing elit, sed do eiusmod</p>
  </div>

  <h2 class="abs section-title">Helpful mental health<br>resources <span class="accent">available</span></h2>
  <div class="abs section-copy">
    <p>Lorem ipsum dolor sit amet, consectetur adipiscing elit, sed do eiusmod tempor incididunt ut labore et dolore magna aliqua.</p>
    <p>Vel risus commodo viverra maecenas accumsan lacus vel facilisis.</p>
  </div>
  <div class="abs btn" style="left:131px;top:1119px;width:100px;height:26px">Go to Resources</div>
  <div class="abs photo-back"></div>
  <div class="abs photo" role="img" aria-label="Photo of a young woman in a knit sweater working on a laptop on a sofa"></div>

  <div class="abs band"></div>
  <h2 class="abs band-title">Ask for <span class="accent">help now</span></h2>
  <p class="abs band-sub">Lorem ipsum dolor sit amet, consectetur adipiscing elit.</p>
  <div class="abs field" style="left:130px;width:149px">First Name</div>
  <div class="abs field" style="left:285px;width:149px">Last Name</div>
  <div class="abs field" style="left:440px;width:150px">Email Address</div>
  <div class="abs btn" style="left:597px;top:1438px;width:108px;height:28px">Submit</div>

  <div class="abs footer">Calm Harbor | All Rights Reserved |&nbsp;<a href="#">Terms and Conditions</a>&nbsp;|&nbsp;<a href="#">Data Protection</a></div>

</div>
</div>
</body>
</html>
```